Business Card Design Project

Need a business card for a web application development company based in Denver Colorado. Our tagline is "Building Your Business, Not Just a Web Site"

Double-sided design with logo, taglin on one side and contact details on other (+ any other design elements).

Can use either or both of our logos (both are attached to project in psd and eps format)

Industry/Entity Type

Business

Requirements
Must have
• Use blue and gray as the main color. Something similar to the color scheme of the home page of our web site (www.northgate-pixel-foundry.com)

```html
<!DOCTYPE html>
<html lang="en">
<head>
<meta charset="utf-8">
<title>Northgate Pixel Foundry – Business Card</title>
<link href="https://fonts.googleapis.com/css2?family=Montserrat:wght@400;600;700&display=swap" rel="stylesheet">
<style>
  :root {
    --backdrop: #1e1e20;
    --card-blue: #45507a;
    --card-gray: #3f3f41;
    --text-white: #ffffff;
    --text-light: #cfcfd1;
    --text-muted: #a9a9ac;
    --divider: #77777a;
  }
  * { box-sizing: border-box; margin: 0; padding: 0; }
  html, body {
    width: 1200px;
    height: 900px;
    overflow: hidden;
    background: var(--backdrop);
    font-family: "Montserrat", Arial, sans-serif;
  }
  .canvas {
    position: relative;
    width: 1200px;
    height: 900px;
  }
  .card {
    position: absolute;
    top: 307px;
    width: 500px;
    height: 286px;
    border-radius: 28px;
    overflow: hidden;
    box-shadow: 0 18px 40px rgba(0,0,0,0.55);
  }
  .card--front { left: 60px; background: var(--card-blue); }
  .card--back  { left: 640px; background: var(--card-gray); }

  /* Front */
  .brand {
    position: absolute;
    display: flex;
    align-items: center;
    gap: 12px;
    font-weight: 700;
    text-transform: uppercase;
    letter-spacing: 0.5px;
  }
  .brand__dot {
    width: 18px;
    height: 18px;
    border-radius: 50%;
    flex: none;
  }
  .card--front .brand {
    left: 70px;
    top: 92px;
    font-size: 30px;
    color: var(--text-white);
  }
  .card--front .brand__dot { background: var(--text-white); }
  .tagline {
    position: absolute;
    left: 0;
    right: 0;
    top: 212px;
    text-align: center;
    font-size: 15px;
    color: var(--text-white);
    text-transform: uppercase;
    letter-spacing: 0.2px;
  }
  .tagline strong { font-weight: 700; }

  /* Back */
  .card--back .brand {
    left: 50px;
    top: 72px;
    font-size: 22px;
    color: var(--text-light);
  }
  .card--back .brand__dot { background: var(--text-light); width: 14px; height: 14px; }
  .person {
    position: absolute;
    left: 50px;
    top: 170px;
  }
  .person__name {
    font-size: 17px;
    font-weight: 700;
    color: var(--text-light);
    text-transform: uppercase;
    letter-spacing: 0.3px;
  }
  .person__role {
    font-size: 10px;
    color: var(--text-muted);
    margin-top: 2px;
  }
  .person__web {
    font-size: 11px;
    color: var(--text-light);
    margin-top: 16px;
  }
  .contact {
    position: absolute;
    left: 268px;
    top: 186px;
    padding-left: 12px;
    border-left: 1px solid var(--divider);
    font-size: 11px;
    line-height: 1.35;
    color: var(--text-light);
  }
  .contact__line strong { font-weight: 700; }
  .contact__address { margin-top: 10px; }
</style>
</head>
<body>
<main class="canvas">
  <section class="card card--front" aria-label="Card front">
    <div class="brand"><span class="brand__dot"></span>Northgate Pixel Foundry</div>
    <p class="tagline"><strong>Building your business,</strong> not just a website!</p>
  </section>

  <section class="card card--back" aria-label="Card back">
    <div class="brand"><span class="brand__dot"></span>Northgate Pixel Foundry</div>
    <div class="person">
      <p class="person__name">Dana Whitfield</p>
      <p class="person__role">Project Manager</p>
      <p class="person__web">www.northgate-pixel-foundry.com</p>
    </div>
    <div class="contact">
      <p class="contact__line">T: 303.555.0148</p>
      <p class="contact__line">E: <strong>lee</strong>@northgate-pixel-foundry.com</p>
      <p class="contact__address">4200 Larkspur Circle Suite 210<br>Brookvale, CO 80099</p>
    </div>
  </section>
</main>
</body>
</html>
```